new roofing company card

New primary business card for roofing company.

Industry/Entity Type

Residential roofing/Specializing in Asphalt and Standing seam metal roofing

Contact Information for Business Card

Phone number is: 484 672 1058 Email: support@fennridgeroofworks.com website: www.fennridgeroofworks.com

Colors
EB3D1F
EC4F4E
F09395
F8D3D4
FCEDEE

```html
<!DOCTYPE html>
<html lang="en">
<head>
<meta charset="UTF-8">
<title>Fennridge Roofworks – Business Card</title>
<link href="https://fonts.googleapis.com/css2?family=Tinos:wght@400;700&display=swap" rel="stylesheet">
<style>
  :root {
    --stage: #333333;
    --card: #ffffff;
    --card-shade: #ececec;
    --ink: #1f1f1f;
    --muted: #444444;
    --red: #c8302a;
    --band: #1e1e1e;
    --rule: #9a9a9a;
  }
  * { margin: 0; padding: 0; box-sizing: border-box; }
  html, body { width: 1200px; height: 900px; overflow: hidden; }
  body {
    background: var(--stage);
    font-family: "Tinos", "Times New Roman", serif;
    position: relative;
  }
  .card {
    position: absolute;
    left: 320px;
    width: 560px;
    height: 320px;
    border-radius: 30px;
    background: linear-gradient(120deg, var(--card) 0%, var(--card) 45%, var(--card-shade) 100%);
    overflow: hidden;
  }
  .card--back { top: 90px; }
  .card--front { top: 480px; }

  .band {
    position: absolute;
    left: 0; right: 0;
    height: 20px;
    background: var(--band);
  }
  .card--back .band { top: 248px; }
  .card--front .band { top: 240px; }

  .band-mark {
    position: absolute;
    background: var(--card);
    color: var(--red);
    font-weight: 700;
    font-size: 15px;
    padding: 3px 8px;
    letter-spacing: 0.5px;
  }
  .card--back .band-mark { top: 245px; left: 340px; }
  .card--front .band-mark { top: 237px; left: 440px; }

  /* back */
  .services {
    position: absolute;
    top: 78px; left: 0; right: 0;
    text-align: center;
  }
  .services__title {
    font-size: 22px;
    font-weight: 700;
    color: var(--ink);
    margin-bottom: 14px;
  }
  .services__text {
    font-size: 19px;
    color: var(--red);
    line-height: 1.2;
  }

  /* front */
  .brand {
    position: absolute;
    left: 40px; top: 92px;
    width: 200px;
    display: flex;
    align-items: center;
    gap: 10px;
  }
  .brand__square {
    width: 22px; height: 22px;
    background: var(--red);
    flex: none;
  }
  .brand__name {
    font-size: 26px;
    font-weight: 700;
    color: var(--ink);
    line-height: 1.05;
    text-transform: uppercase;
  }
  .divider {
    position: absolute;
    left: 252px; top: 40px;
    width: 1px; height: 170px;
    background: var(--rule);
  }
  .person {
    position: absolute;
    left: 276px; top: 46px;
  }
  .person__name {
    font-size: 20px;
    font-weight: 700;
    color: var(--red);
    letter-spacing: 0.5px;
  }
  .person__role {
    font-size: 16px;
    color: var(--muted);
    margin-top: 2px;
  }
  .contacts {
    list-style: none;
    margin-top: 14px;
  }
  .contacts li {
    display: flex;
    align-items: center;
    gap: 8px;
    font-size: 15.5px;
    color: var(--muted);
    margin-bottom: 5px;
  }
  .contacts svg { width: 15px; height: 15px; flex: none; }
  .accent { color: var(--red); }
</style>
</head>
<body>

<section class="card card--back" aria-label="Card back">
  <div class="services">
    <h2 class="services__title">Our Services</h2>
    <p class="services__text">Residential Roofing Specializing In Asphalt And<br>Standing Seam Metal Roofing</p>
  </div>
  <div class="band"></div>
  <span class="band-mark">Fennridge</span>
</section>

<section class="card card--front" aria-label="Card front">
  <div class="brand">
    <span class="brand__square"></span>
    <span class="brand__name">Fennridge<br>Roofworks</span>
  </div>
  <div class="divider"></div>
  <div class="person">
    <h1 class="person__name">DALE MERROW</h1>
    <p class="person__role">Director</p>
    <ul class="contacts">
      <li>
        <svg viewBox="0 0 16 16" aria-hidden="true"><path fill="#c8302a" d="M3.6 1.5l2.2 2.6-1.3 1.6c.9 2 2.4 3.5 4.4 4.4l1.6-1.3 2.6 2.2-1.2 2.4C7 13.2 2.8 9 1.2 2.7z"/></svg>
        <span>484 672 1058</span>
      </li>
      <li>
        <svg viewBox="0 0 16 16" aria-hidden="true"><rect x="1" y="3" width="14" height="10" fill="#c8302a"/><path d="M1.5 3.5L8 9l6.5-5.5" fill="none" stroke="#fff" stroke-width="1.3"/></svg>
        <span>support@<span class="accent">fennridgeroofworks</span>.com</span>
      </li>
      <li>
        <svg viewBox="0 0 16 16" aria-hidden="true"><g fill="none" stroke="#c8302a" stroke-width="1.3"><circle cx="8" cy="8" r="6.5"/><ellipse cx="8" cy="8" rx="2.8" ry="6.5"/><path d="M1.5 8h13M2.6 4.8h10.8M2.6 11.2h10.8"/></g></svg>
        <span>www.<span class="accent">fennridgeroofworks</span>.com</span>
      </li>
    </ul>
  </div>
  <div class="band"></div>
  <span class="band-mark">Fennridge</span>
</section>

</body>
</html>
```